Business Card Design Project

Basic business card with minimal details. I just need company name, email & web address, telephone and my name.
I would like the back of the card to be grey with my logo & company name centred.

Target Market(s)

Architects
Builders
Property Developers

Industry/Entity Type

Business

Font styles to use
Sans Serif

Colors

Designer to choose colors to be used in the design.

Requirements
Must have
• Framewise Build
Marcus Helby - Director
M: 0427 593184
E: marcus@framewisebuild.com.au
W: www.framewisebuild.com.au
Should not have
• No other images or pictures

```html
<!DOCTYPE html>
<html lang="en">
<head>
<meta charset="utf-8">
<title>Framewise Build – Business Card</title>
<link rel="stylesheet" href="https://fonts.googleapis.com/css2?family=Roboto:wght@400;500;700&display=swap">
<style>
  :root {
    --backdrop: #242424;
    --card-front: #e4e3e1;
    --card-back: #b7bbbd;
    --glow: #f4f4f4;
    --ink: #1d1d1d;
    --slate: #4b5967;
    --brand-red: #b3262f;
    --label: #e4502c;
    --rule: #2d2d2d;
  }
  * { margin: 0; padding: 0; box-sizing: border-box; }
  html, body {
    width: 1200px; height: 900px; overflow: hidden;
    background: var(--backdrop);
    font-family: "Roboto", Arial, sans-serif;
  }
  .stage { position: relative; width: 1200px; height: 900px; }

  .card {
    position: absolute;
    width: 600px; height: 366px;
    border-radius: 3px;
    box-shadow: 0 10px 24px rgba(0,0,0,.55);
  }
  .card--front { left: 140px; top: 70px; background: var(--card-front); }
  .card--back {
    left: 460px; top: 470px;
    background: radial-gradient(circle at 50% 52%, var(--glow) 0, #d6d8d9 22%, var(--card-back) 48%);
  }

  .holder { position: absolute; right: 46px; top: 38px; text-align: right; }
  .holder__name { font-size: 25px; font-weight: 700; color: var(--ink); letter-spacing: .2px; }
  .holder__role { font-size: 17px; color: var(--ink); margin-top: 1px; }

  .brand { display: flex; align-items: center; gap: 12px; }
  .brand__mark { width: 20px; height: 20px; background: var(--brand-red); }
  .brand__name {
    font-size: 22px; font-weight: 400; color: var(--slate);
    letter-spacing: 2px; text-transform: uppercase;
  }
  .card--front .brand { position: absolute; left: 56px; top: 138px; }
  .card--back .brand { position: absolute; left: 50%; top: 50%; transform: translate(-50%, -50%); }

  .rule {
    position: absolute; left: 96px; right: 60px; top: 236px;
    height: 6px; background: var(--rule);
  }
  .contact {
    position: absolute; left: 100px; right: 60px; top: 262px;
    text-align: center; font-size: 16px; color: var(--ink); line-height: 30px;
  }
  .contact__label { color: var(--label); }
</style>
</head>
<body>
<main class="stage">
  <section class="card card--front" aria-label="Business card front">
    <div class="holder">
      <p class="holder__name">Marcus Helby</p>
      <p class="holder__role">Director</p>
    </div>
    <div class="brand">
      <span class="brand__mark"></span>
      <span class="brand__name">Framewise Build</span>
    </div>
    <div class="rule"></div>
    <div class="contact">
      <p><span class="contact__label">Phone:</span>0427 593184 <span class="contact__label">Email:</span> marcus@framewisebuild.com.au</p>
      <p><span class="contact__label">Website:</span> www.framewisebuild.com.au</p>
    </div>
  </section>

  <section class="card card--back" aria-label="Business card back">
    <div class="brand">
      <span class="brand__mark"></span>
      <span class="brand__name">Framewise Build</span>
    </div>
  </section>
</main>
</body>
</html>
```